Post announcing a new website

Please prepare a poster to announce Harbourline Tavern's new website and Marlow's Asian Kitchen online ordering system.

The poster (A3) should have space in the bottom third for text in multiple languages.

Please use www.harbourlinetavern.com.au as a guide to style

Thanks all, I have sent these designs to the client and will get back to you shortly.

```html
<!DOCTYPE html>
<html lang="en">
<head>
<meta charset="utf-8">
<title>Harbourline Tavern – New Website Poster</title>
<link href="https://fonts.googleapis.com/css2?family=Open+Sans:wght@400;600;700;800&display=swap" rel="stylesheet">
<style>
  :root {
    --black: #0b0b0b;
    --yellow: #f7c416;
    --yellow-dark: #e8a60c;
    --red: #d7141a;
    --red-dark: #a50d12;
    --white: #ffffff;
    --grey-text: #b9b9b9;
    --device: #161616;
    --site-dark: #1c1c1c;
  }
  * { margin: 0; padding: 0; box-sizing: border-box; }
  html, body { width: 849px; height: 1200px; overflow: hidden; background: var(--black); }
  .poster {
    position: relative; width: 849px; height: 1200px; overflow: hidden;
    background: var(--black); font-family: "Open Sans", Arial, sans-serif; color: var(--white);
  }
  .brand {
    position: absolute; top: 48px; left: 0; width: 100%;
    display: flex; justify-content: center; align-items: center; gap: 16px;
  }
  .brand-mark { width: 34px; height: 34px; border-radius: 50%; background: var(--red); }
  .brand-name { font-size: 46px; font-weight: 700; color: var(--yellow); letter-spacing: -0.5px; }
  .headline {
    position: absolute; top: 182px; width: 100%; text-align: center;
    font-size: 34px; font-weight: 800; color: var(--yellow);
  }
  .intro {
    position: absolute; top: 238px; left: 95px; width: 660px; text-align: center;
    font-size: 13.5px; font-weight: 700; line-height: 1.5;
  }
  .order-band {
    position: absolute; top: 318px; left: 0; width: 100%; height: 166px;
    background: linear-gradient(180deg, var(--red) 0%, var(--red-dark) 100%);
    border-top: 12px solid var(--yellow);
  }
  .order-icon { position: absolute; left: 112px; top: 22px; width: 96px; height: 110px; }
  .order-title {
    position: absolute; left: 240px; top: 24px;
    font-size: 44px; font-weight: 800; line-height: 1.2;
  }

  /* showcase scene */
  .showcase {
    position: absolute; top: 484px; left: 0; width: 100%; height: 470px;
    background:
      radial-gradient(ellipse 90px 110px at 40px 170px, rgba(214,40,40,.85), rgba(214,40,40,0) 100%),
      radial-gradient(ellipse 120px 90px at 800px 130px, rgba(255,255,255,.9), rgba(255,255,255,0) 100%),
      linear-gradient(180deg, #e9e6e2 0%, #cfcac4 60%, #a9a39c 100%);
  }
  .tablet {
    position: absolute; top: 506px; left: 152px; width: 580px; height: 452px;
    background: var(--device); border-radius: 26px; padding: 30px 34px;
    box-shadow: 0 10px 30px rgba(0,0,0,.45);
  }
  .site { width: 100%; height: 100%; background: var(--site-dark); overflow: hidden; position: relative; }
  .site-header {
    height: 58px; display: flex; align-items: center; justify-content: space-between;
    padding: 0 18px; background: #101010;
  }
  .site-brand { font-size: 17px; font-weight: 700; color: var(--yellow); }
  .site-contact { display: flex; flex-direction: column; gap: 5px; }
  .site-contact span { display: block; width: 78px; height: 4px; background: #555; }
  .site-nav {
    height: 22px; background: linear-gradient(180deg, var(--yellow), var(--yellow-dark));
    display: flex; align-items: center; gap: 18px; padding: 0 18px;
    font-size: 9px; font-weight: 700; color: #2a2a2a;
  }
  .site-hero {
    position: absolute; top: 92px; left: 10px; right: 10px; bottom: 10px;
    background: linear-gradient(135deg, #f1efe9 0%, #d9d2c3 35%, #b79a5a 55%, #6e7d3a 70%, #e9e4da 100%);
  }
  .site-panel {
    position: absolute; top: 112px; left: 22px; width: 190px; height: 250px;
    background: rgba(20,20,20,.88); padding: 16px 14px;
  }
  .site-panel h4 { font-size: 14px; font-weight: 700; color: var(--yellow); line-height: 1.3; margin-bottom: 12px; }
  .site-panel span { display: block; height: 4px; background: #666; margin-bottom: 7px; }

  .accent-stripe {
    position: absolute; top: 954px; left: 0; width: 100%; height: 18px;
    background: linear-gradient(180deg, var(--yellow) 0%, var(--yellow-dark) 100%);
  }
  .info-title {
    position: absolute; top: 1004px; left: 110px;
    font-size: 20px; font-weight: 700;
  }
  .info-body {
    position: absolute; top: 1046px; left: 110px; width: 630px;
    font-size: 13px; line-height: 1.55; color: var(--grey-text);
  }
</style>
</head>
<body>
<main class="poster">
  <header class="brand">
    <span class="brand-mark"></span>
    <span class="brand-name">Harbourline Tavern</span>
  </header>

  <h1 class="headline">Harbourline Tavern &amp; Restaurant.</h1>
  <p class="intro">5 Star Scores on Clean Plate Rating, great food, clean kitchen and fresh ingredients. Quality Asian food located in the inner city. kitchen and fresh ingredients. Quality Asian food located in the inner city.</p>

  <section class="order-band">
    <svg class="order-icon" viewBox="0 0 96 110" aria-hidden="true">
      <circle cx="46" cy="44" r="36" fill="#111"/>
      <path d="M10 44 a36 36 0 0 1 72 0" fill="none" stroke="#111" stroke-width="8"/>
      <rect x="4" y="36" width="14" height="26" rx="5" fill="#111"/>
      <rect x="74" y="36" width="14" height="26" rx="5" fill="#111"/>
      <path d="M14 62 q4 26 30 26" fill="none" stroke="#111" stroke-width="4"/>
      <rect x="40" y="82" width="14" height="10" rx="4" fill="#111"/>
      <path d="M18 110 q28 -30 56 0 z" fill="#111"/>
    </svg>
    <h2 class="order-title">Marlow's Asian Kitchen<br>online ordering system.</h2>
  </section>

  <div class="showcase" role="img" aria-label="Photo backdrop with red flowers on the left and a plated Asian dish on the right"></div>

  <div class="tablet">
    <div class="site">
      <div class="site-header">
        <span class="site-brand">Harbourline Tavern</span>
        <div class="site-contact"><span></span><span></span><span></span></div>
      </div>
      <nav class="site-nav">
        <span>Home</span><span>About Us</span><span>Order Online</span><span>News</span><span>Events</span><span>Contact Us</span>
      </nav>
      <div class="site-hero" role="img" aria-label="Photo of an Asian dish with fresh vegetables"></div>
      <div class="site-panel">
        <h4>Harbourline Tavern &amp; Restaurant</h4>
        <span></span><span></span><span></span><span style="width:70%"></span>
      </div>
    </div>
  </div>

  <div class="accent-stripe"></div>

  <h3 class="info-title">Koin gravida nibh vel velit auctor aliquet.</h3>
  <p class="info-body">Aenean sollicitudin, lorem quis bibendum  ctor, nisi elit consequat ipsum, nec sagittis sem nibh id elit. Duis sed odio sit amet nibh vulputate cursus a sit amet mauris. Morbi accumsan ipsum velit. Nam nec tellus a odio tincidunt auctor a ornare odio. Sed non  mauris vitae erat consequat auctor eu in elit. Class aptent tit sociosqu ad litora torquent per conubia nostra, per inceptos himenaeos. Mauris in erat justo. Nullam ac urna eu felis dapibus condimentum sit amet a augue. Sed non neque elit. Sed ut imperdiet nisi. Proin condimentum fermentum nunc. Etiam pharetra, erat sed fermentum</p>
</main>
</body>
</html>
```